Android App Design for Travel Agency

[login to view URL] needs a new Android App.

We are not only looking for a layout but also for an user-interaction design.

Screens should include:
Startscreen
Search-Form Screen
Search-Result Screen
Hotel Details & Rate Details
Booking-Form Screen
About Page
Reservation-Screen (to see reservation-details)
and some more like dialogs and tabs and Launcher Icon

The design should derive from the website design [login to view URL]

Also part of the package is the provision of Android specific artifacts: All designs in 3-5 different dpi, depending on device-display-resolutions and sizes.
Splicing of graphics for use in Android Development.

ATTENTION: We do not need a new corporate design! Current logo on [login to view URL] has to be used as it is for the new android application. New CIs like logos and maybe even color combinations will not be considered.

EDIT: Attached screenshot of website-search-result for reference. App should cover as much information as possible while of course preserving read-/usability.

EDIT2: Customer likes to have a Flat Design. Please consider this when layouting.

EDIT3: Guaranteed! So far proposals are quite convincing. We are positive that we'll get our needed design.

```html
<!DOCTYPE html>
<html lang="en">
<head>
<meta charset="utf-8">
<title>Lanternway – Start</title>
<link rel="stylesheet" href="https://fonts.googleapis.com/css2?family=Arimo:wght@400;700&display=swap">
<style>
  :root {
    --sky-top: #4a1fae;
    --sky-mid: #6a2cc4;
    --sky-glow: #b04ac8;
    --city-dark: #1c1230;
    --city-warm: #6a4a3a;
    --text-white: #ffffff;
    --pill-fill: rgba(255, 255, 255, 0.26);
    --pill-edge: rgba(255, 255, 255, 0.18);
    --flight-blue: #3899e9;
    --hotel-green: #33b14f;
  }
  * { box-sizing: border-box; margin: 0; padding: 0; }
  html, body { width: 675px; height: 1200px; overflow: hidden; background: var(--city-dark); }
  .screen {
    position: relative;
    width: 675px;
    height: 1200px;
    overflow: hidden;
    font-family: "Arimo", Arial, sans-serif;
    color: var(--text-white);
  }
  .backdrop {
    position: absolute;
    inset: 0;
    background:
      radial-gradient(ellipse 60% 18% at 50% 88%, rgba(230, 170, 110, 0.55), transparent 70%),
      radial-gradient(ellipse 45% 20% at 85% 52%, rgba(210, 90, 200, 0.55), transparent 70%),
      linear-gradient(180deg, var(--sky-top) 0%, var(--sky-mid) 30%, var(--sky-glow) 50%, #3a2260 62%, var(--city-dark) 78%, var(--city-warm) 92%, #2a1c2c 100%);
  }
  .status-bar {
    position: absolute;
    top: 0; left: 0; right: 0;
    height: 38px;
    display: flex;
    align-items: center;
    padding: 0 14px;
    font-size: 21px;
    font-weight: 400;
  }
  .status-left { display: flex; align-items: center; gap: 6px; flex: 1; }
  .signal-dots { display: flex; gap: 3px; }
  .signal-dots span { width: 9px; height: 9px; border-radius: 50%; background: var(--text-white); }
  .status-time { position: absolute; left: 0; right: 0; text-align: center; pointer-events: none; }
  .battery {
    width: 48px; height: 19px;
    border: 2px solid var(--text-white);
    border-radius: 4px;
    padding: 2px;
    position: relative;
  }
  .battery::before { content: ""; display: block; width: 100%; height: 100%; background: var(--text-white); border-radius: 1px; }
  .battery::after { content: ""; position: absolute; right: -5px; top: 4px; width: 3px; height: 7px; background: var(--text-white); border-radius: 0 2px 2px 0; }
  .brand-name {
    position: absolute;
    top: 166px; left: 0; right: 0;
    text-align: center;
    font-family: "Arimo", Arial, sans-serif;
    font-weight: 700;
    font-size: 64px;
    line-height: 1;
    color: var(--text-white);
  }
  .menu-pill {
    position: absolute;
    left: 16px;
    width: 643px;
    height: 147px;
    border-radius: 74px;
    background: var(--pill-fill);
    border: 1px solid var(--pill-edge);
    font-size: 31px;
    font-weight: 700;
    text-shadow: 0 1px 3px rgba(0, 0, 0, 0.45);
  }
  .menu-pill--flight { top: 827px; }
  .menu-pill--hotel { top: 987px; }
  .pill-label {
    position: absolute;
    left: 0; right: 0;
    top: 50%;
    transform: translateY(-50%);
    text-align: center;
    line-height: 1;
  }
  .pill-icon {
    position: absolute;
    top: 1px;
    width: 143px;
    height: 143px;
    border-radius: 50%;
    display: flex;
    align-items: center;
    justify-content: center;
    border: 2px solid rgba(255, 255, 255, 0.35);
  }
  .menu-pill--flight .pill-icon { right: 0; background: var(--flight-blue); }
  .menu-pill--hotel .pill-icon { left: 0; background: var(--hotel-green); }
</style>
</head>
<body>
<main class="screen">
  <div class="backdrop" role="img" aria-label="Blurred photo of a city skyline at dusk with purple sky and warm waterfront lights"></div>

  <header class="status-bar">
    <div class="status-left">
      <div class="signal-dots"><span></span><span></span><span></span><span></span><span></span></div>
      <span class="carrier">Signal</span>
      <svg width="22" height="17" viewBox="0 0 22 17" aria-hidden="true">
        <path d="M11 16 L8 12.6 A4.5 4.5 0 0 1 14 12.6 Z" fill="#fff"/>
        <path d="M4.8 9.2 A9 9 0 0 1 17.2 9.2" stroke="#fff" stroke-width="2.4" fill="none"/>
        <path d="M1.5 5.6 A13.5 13.5 0 0 1 20.5 5.6" stroke="#fff" stroke-width="2.4" fill="none"/>
      </svg>
    </div>
    <div class="status-time">9:41 AM</div>
    <div class="battery"></div>
  </header>

  <h1 class="brand-name">Lanternway</h1>

  <nav>
    <a class="menu-pill menu-pill--flight">
      <span class="pill-label">FLIGHT</span>
      <span class="pill-icon">
        <svg width="92" height="92" viewBox="0 0 24 24" aria-hidden="true">
          <path fill="#fff" d="M12 1.5c.8 0 1.3 1 1.3 2.2v5.6l8.7 5v2l-8.7-2.6v4.8l2.4 1.8V22L12 21l-3.7 1v-1.7l2.4-1.8v-4.8L2 15.3v-2l8.7-5V3.7c0-1.2.5-2.2 1.3-2.2z"/>
        </svg>
      </span>
    </a>
    <a class="menu-pill menu-pill--hotel">
      <span class="pill-label">HOTEL</span>
      <span class="pill-icon">
        <svg width="74" height="86" viewBox="0 0 74 86" aria-hidden="true">
          <g fill="#fff">
            <polygon points="20,2 22.4,7 28,7.4 23.7,10.8 25.2,16 20,13 14.8,16 16.3,10.8 12,7.4 17.6,7"/>
            <polygon points="37,2 39.4,7 45,7.4 40.7,10.8 42.2,16 37,13 31.8,16 33.3,10.8 29,7.4 34.6,7"/>
            <polygon points="54,2 56.4,7 62,7.4 57.7,10.8 59.2,16 54,13 48.8,16 50.3,10.8 46,7.4 51.6,7"/>
          </g>
          <path fill="#fff" fill-rule="evenodd" d="M4 20h66v64H4z M11 27v10h12V27z M31 27v10h12V27z M51 27v10h12V27z M11 43v10h12V43z M31 43v10h12V43z M51 43v10h12V43z M11 59v10h12V59z M51 59v10h12V59z M31 59v19h12V59z"/>
        </svg>
      </span>
    </a>
  </nav>
</main>
</body>
</html>
```